New Business Card Design Project

I need a meaningful new business card. Therefore, the website should convey growth, joy, uniqueness, workout and a bit of luxury.
Color scheme should be petrol, gold and matching colors.

```html
<!DOCTYPE html>
<html lang="en">
<head>
<meta charset="utf-8">
<title>Corebloom Studio – Business Card</title>
<link href="https://fonts.googleapis.com/css2?family=Great+Vibes&family=Lato:wght@400;700&display=swap" rel="stylesheet">
<style>
  :root {
    --backdrop: #1b1c1d;
    --petrol-deep: #173338;
    --petrol: #1f4a50;
    --card: #222526;
    --gold: #d4a93c;
    --gold-light: #f0cd6a;
    --text-soft: #d6d6d6;
  }
  * { box-sizing: border-box; margin: 0; padding: 0; }
  html, body {
    width: 1200px; height: 939px; overflow: hidden;
    background: var(--backdrop);
    font-family: "Lato", sans-serif;
  }
  .canvas { position: relative; width: 1200px; height: 939px; }
  .card {
    position: absolute;
    width: 560px; height: 320px;
    border-radius: 16px;
    background: linear-gradient(135deg, var(--petrol-deep) 0%, var(--card) 70%);
    border: 2px solid var(--gold);
    box-shadow: 0 18px 40px rgba(0, 0, 0, 0.45);
  }
  .card--front { left: 90px; top: 90px; }
  .card--back { left: 550px; top: 520px; }

  .brand-area {
    position: absolute;
    display: flex; align-items: center; justify-content: center;
  }
  .card--front .brand-area { inset: 0; }
  .card--back .brand-area { left: 0; top: 0; bottom: 0; width: 270px; }

  .brand {
    display: flex; align-items: center; gap: 10px;
    white-space: nowrap;
    color: var(--gold);
    font-family: "Lato", sans-serif;
    font-weight: 700;
    letter-spacing: 0.04em;
  }
  .brand__dot {
    width: 14px; height: 14px; border-radius: 50%;
    background: var(--petrol);
    border: 2px solid var(--gold);
    flex: none;
  }
  .card--front .brand { font-size: 32px; }
  .card--back .brand { font-size: 21px; }

  .contact { position: absolute; left: 280px; top: 40px; right: 24px; }
  .contact__name {
    font-family: "Great Vibes", cursive;
    font-size: 42px; line-height: 1;
    color: var(--gold-light);
    white-space: nowrap;
  }
  .contact__role { font-size: 14px; color: var(--text-soft); margin-top: 4px; }
  .contact__rule { width: 26px; height: 2px; background: var(--gold); margin: 14px 0 16px; }
  .contact__list { list-style: none; }
  .contact__item {
    display: flex; align-items: flex-start; gap: 10px;
    font-size: 13px; line-height: 1.45; color: var(--text-soft);
    margin-bottom: 4px;
    white-space: nowrap;
  }
  .contact__icon { width: 12px; height: 12px; margin-top: 3px; flex: none; fill: var(--gold); }
</style>
</head>
<body>
<main class="canvas">
  <section class="card card--front" aria-label="Card front">
    <div class="brand-area">
      <div class="brand"><span class="brand__dot"></span>Corebloom Studio</div>
    </div>
  </section>

  <section class="card card--back" aria-label="Card back">
    <div class="brand-area">
      <div class="brand"><span class="brand__dot"></span>Corebloom Studio</div>
    </div>
    <div class="contact">
      <p class="contact__name">Lena Harwick</p>
      <p class="contact__role">Pilates Instructior</p>
      <div class="contact__rule"></div>
      <ul class="contact__list">
        <li class="contact__item">
          <svg class="contact__icon" viewBox="0 0 12 12"><path d="M6 0a4 4 0 0 0-4 4c0 3 4 8 4 8s4-5 4-8a4 4 0 0 0-4-4zm0 5.5A1.5 1.5 0 1 1 6 2.5a1.5 1.5 0 0 1 0 3z"/></svg>
          <span>123 Street Address<br>City, State, Zip</span>
        </li>
        <li class="contact__item">
          <svg class="contact__icon" viewBox="0 0 12 12"><path d="M2.5 0.5 4.5 3 3.5 4.5c.8 1.6 2 2.8 3.5 3.5L8.5 7l2.5 2-1 2.3C5 11 1 7 .7 1.5z"/></svg>
          <span>+10 123 456 789</span>
        </li>
        <li class="contact__item">
          <svg class="contact__icon" viewBox="0 0 12 12"><path d="M0 2h12v8H0zm1 1v.3l5 3.2 5-3.2V3z"/></svg>
          <span>info@corebloomstudio.com</span>
        </li>
        <li class="contact__item">
          <svg class="contact__icon" viewBox="0 0 12 12"><circle cx="6" cy="6" r="5.5"/><path d="M.5 6h11M6 .5c-2 2-2 9 0 11M6 .5c2 2 2 9 0 11" stroke="#1f4a50" stroke-width=".8" fill="none"/></svg>
          <span>corebloomstudio.com</span>
        </li>
      </ul>
    </div>
  </section>
</main>
</body>
</html>
```